Banner Ad Design Project

We are re-branding our energy management company called 'Voltrix'. We sell Energy Management Information Software and are currently positioned as a very technical organization. While we are always going to be very technical we want to shift away from telling people about the power of our software and become a more customer centric organization focusing on how energy management can solve many of your organizations problems. The final design should be modern and simple, as we are taking something very technical and complicated and trying to sell it. We need 4 banners created for our site www.voltrix-example.com which rotate across the top. They all need to be different and easily editable (preferably Photoshop)as we change marketing campaigns, the text needs to be editable.

The Size of the banners are 940 pixels by 250 pixels.
Updates

Thank you so much to everyone for you questions and for the few designs I have received. I am very new at this so please if there are things I can do to help better convey my design needs please let me know. Many people have asked for the Text to do on the banners. Here is what I have come up with for the 4 banners.

Banner 1

Maintain high building standards
                - With lower energy costs

Banner 2
Energy Reporting Requirements
                - Made effortless

Banner 3
Presenting Colin Parsons, President of RDLMS, June 19th
- The future of Ontario’s power market

Banner 4
Working with utilities to develop and execute successful Energy Conservation Programs

As well we are working on re-branding ourselves so the website at this point does not convey the look and feel we are looking to go with. The attached files, especially the brochure and business card, convey the look and feel I am looking fore much better!

Reason: Need to check with the rest of my team to make final decision. Keep submitting designs, Thanks!

Industry/Entity Type

Marketing

Requirements
Must have
• The size needs to be 940 by 250 pixels. They need to contain the green color indicated in the 'Voltrix branding design features' document.

Needs to be consistent withe the look and feel of the brochure, PowerPoint and business card attached.

The integration of the 'Voltrix Head' and other similar graphics into the banners.
Should not have
• The look and feel of our current website

```html
<!DOCTYPE html>
<html lang="en">
<head>
<meta charset="utf-8">
<title>Voltrix banner set</title>
<link href="https://fonts.googleapis.com/css2?family=Arvo:wght@700&family=Open+Sans:wght@400;600;700&display=swap" rel="stylesheet">
<style>
  :root{
    --leaf:#86c03f;
    --forest:#1b6435;
    --paper:#ffffff;
    --stage:#ececec;
    --art-soft:#9fcd62;
    --art-pale:#e4f0d5;
  }
  *{box-sizing:border-box;margin:0;padding:0}
  html,body{width:1200px;height:1000px;overflow:hidden}
  body{background:var(--stage);position:relative;font-family:"Open Sans",Arial,sans-serif}
  .banner{position:absolute;left:196px;width:866px;height:230px;background:var(--leaf);overflow:hidden;color:var(--paper)}
  .banner--standards{top:10px}
  .banner--reporting{top:254px}
  .banner--event{top:498px}
  .banner--programs{top:749px}
  .abs{position:absolute;z-index:2;white-space:nowrap}
  .slab{font-family:"Arvo",Georgia,serif;font-weight:700;line-height:1.05}
  .dark{color:var(--forest)}
  .light{color:var(--leaf)}
  .white{color:var(--paper)}
  .brand{position:absolute;z-index:2;display:flex;flex-direction:column;align-items:center;font-family:"Open Sans",Arial,sans-serif;font-weight:700;color:var(--paper);line-height:1}
  .brand__dot{width:32px;height:32px;border-radius:50%;background:var(--forest);margin-bottom:4px}
  .brand--small .brand__dot{width:14px;height:14px;margin-bottom:2px}
  .tagline{position:absolute;z-index:2;font-size:6.5px;font-weight:700;letter-spacing:.2px;text-transform:uppercase}
  .art{position:absolute;z-index:1;border-radius:70px 70px 8px 8px}
  /* banner 1 */
  .standards__white{position:absolute;left:520px;top:0;width:346px;height:230px;background:var(--paper)}
  .standards__headline{left:72px;top:70px;font-size:28.5px;line-height:0.9}
  .standards__lower{left:645px;top:62px;font-size:46px}
  .standards__costs{left:647px;top:108px;font-size:19px;font-weight:600;letter-spacing:1px;color:var(--forest)}
  .standards__dash{position:absolute;left:632px;top:140px;width:204px;border-top:2px dashed var(--leaf)}
  /* banner 2 */
  .reporting__headline{left:290px;top:30px;font-size:28px}
  .reporting__made{left:486px;top:88px;font-size:46px}
  .reporting__effortless{left:488px;top:134px;font-size:17px;letter-spacing:2.5px;border-bottom:2px dashed var(--paper);padding-bottom:2px}
  /* banner 3 */
  .event__white{position:absolute;left:0;top:0;width:420px;height:230px;background:var(--paper)}
  .event__day{left:124px;top:14px;font-size:90px}
  .event__th{left:220px;top:64px;font-size:28px}
  .event__month{left:130px;top:96px;font-size:24px;letter-spacing:16px}
  .event__speaker{left:10px;top:140px;font-size:24px}
  .event__role{left:10px;top:172px;font-size:17px}
  .event__topic{left:517px;top:146px;font-size:26px;line-height:0.95}
  /* banner 4 */
  .programs__copy{left:28px;top:24px;font-size:27.5px;line-height:1.02}
</style>
</head>
<body>

<section class="banner banner--standards">
  <div class="standards__white"></div>
  <h2 class="abs slab standards__headline white">MAINTAIN <span class="dark">HIGH</span><br>BUILDING STANDARDS</h2>
  <div class="brand" style="left:124px;top:148px;font-size:30px"><span class="brand__dot"></span>voltrix</div>
  <div class="art" role="img" aria-label="Outline head graphic with a light bulb inside" style="left:425px;top:10px;width:165px;height:220px;background:var(--art-pale)"></div>
  <svg class="abs" style="left:612px;top:68px" width="24" height="60" viewBox="0 0 24 60" aria-hidden="true">
    <line x1="12" y1="0" x2="12" y2="54" stroke="#86c03f" stroke-width="3"/>
    <polyline points="2,44 12,56 22,44" fill="none" stroke="#86c03f" stroke-width="3"/>
  </svg>
  <div class="abs slab standards__lower dark">LOWER</div>
  <div class="abs standards__costs">ENERGY COSTS</div>
  <div class="standards__dash"></div>
  <div class="tagline light" style="left:630px;top:208px">Voltrix | Enabling the intelligent use of energy</div>
</section>

<section class="banner banner--reporting">
  <div class="art" role="img" aria-label="Light bulb with rays above two outline heads" style="left:190px;top:12px;width:72px;height:72px;border-radius:50%;background:var(--art-soft)"></div>
  <div class="art" role="img" aria-label="Two outline heads facing each other, one with a dark green circle" style="left:60px;top:92px;width:230px;height:138px;background:var(--art-soft)"></div>
  <h2 class="abs slab reporting__headline white"><span class="dark">ENERGY</span> REPORTING REQUIREMENTS</h2>
  <div class="art" role="img" aria-label="Flame icon" style="left:432px;top:94px;width:46px;height:62px;border-radius:50% 50% 40% 40%;background:var(--art-soft)"></div>
  <div class="abs slab reporting__made dark">MADE</div>
  <div class="abs reporting__effortless">EFFORTLESS</div>
  <div class="brand brand--small" style="left:8px;top:196px;font-size:14px"><span class="brand__dot"></span>voltrix</div>
  <div class="tagline white" style="left:640px;top:210px">Voltrix | Enabling the intelligent use of energy</div>
</section>

<section class="banner banner--event">
  <div class="event__white"></div>
  <div class="art" role="img" aria-label="Gear icons" style="left:6px;top:6px;width:84px;height:82px;border-radius:50%;background:var(--art-pale)"></div>
  <div class="abs slab event__day dark">19</div>
  <div class="abs slab event__th dark">TH</div>
  <div class="abs slab event__month light">JUNE</div>
  <div class="abs slab event__speaker dark">PRESENTING <span class="light">Colin Parsons</span></div>
  <div class="abs slab event__role dark">PRESIDENT OF <span class="light">RDLMS</span></div>
  <div class="art" role="img" aria-label="Large outline light bulb" style="left:365px;top:0;width:130px;height:230px;border-radius:65px 65px 20px 20px;background:var(--art-soft)"></div>
  <div class="brand" style="left:532px;top:66px;font-size:30px"><span class="brand__dot"></span>voltrix</div>
  <div class="abs slab event__topic white">The future of<br>Ontario’s power market</div>
  <div class="tagline white" style="left:640px;top:210px">Voltrix | Enabling the intelligent use of energy</div>
</section>

<section class="banner banner--programs">
  <p class="abs slab programs__copy white">Working with utilities<br>to develop and execute successful<br><span class="dark">Energy Conservation Programs</span></p>
  <div class="brand" style="left:160px;top:146px;font-size:30px"><span class="brand__dot"></span>voltrix</div>
  <div class="art" role="img" aria-label="Outline house roofline leading into a head with a light bulb" style="left:490px;top:4px;width:376px;height:226px;border-radius:8px 90px 0 0;background:var(--art-soft)"></div>
</section>

</body>
</html>
```